Business card design for my trucking company

I would like a business card designed for my new trucking company. Please use my logo. the rest of the design is up to you. i would like my clients to say wow when they see the card. Im looking forward to seeing your designs

Target Market(s)

Industry/Entity Type

Trucking Company

Contact Information for Business Card

Marcus Tillbrook President
518-555-0147
ridgelinehaulingcompany@postvane.com

Font styles to use
Serif

Requirements
Must have
• my logo, name and number. we are located in Schenectady New York. the rest is up to you
Nice to have
• up to you
Should not have
• none

```html
<!DOCTYPE html>
<html lang="en">
<head>
<meta charset="utf-8">
<title>Ridgeline Hauling – Business Card</title>
<link href="https://fonts.googleapis.com/css2?family=Roboto:wght@400;700;900&display=swap" rel="stylesheet">
<style>
  :root {
    --backdrop: #3a3a3a;
    --card: #1f1f1f;
    --card-back: #222222;
    --accent: #e3202a;
    --ink-light: #f2f2f2;
    --ink-muted: #8a8a8a;
    --emboss: #121212;
  }
  * { box-sizing: border-box; margin: 0; padding: 0; }
  html, body {
    width: 1200px; height: 801px; overflow: hidden;
    background: var(--backdrop);
    font-family: "Roboto", Arial, sans-serif;
  }
  .stage {
    position: relative; width: 1200px; height: 801px;
    display: flex; align-items: center; justify-content: center; gap: 50px;
  }
  .card {
    position: relative; width: 525px; height: 300px;
    background: var(--card);
    border-bottom: 3px solid var(--accent);
    border-left: 1px solid var(--accent);
    box-shadow: 0 18px 40px rgba(0,0,0,.45);
  }
  .card--back { background: var(--card-back); }

  .wordmark {
    position: absolute; left: 0; right: 0; top: 62px;
    text-align: center; color: var(--accent);
    font-weight: 900; text-transform: uppercase; line-height: 1.05;
  }
  .wordmark__main { display: block; font-size: 44px; letter-spacing: 1px; }
  .wordmark__sub { display: block; font-size: 15px; letter-spacing: 3px; margin-top: 6px; }
  .card--back .wordmark { top: 100px; color: var(--emboss); }

  .contact-block {
    position: absolute; left: 36px; right: 28px; bottom: 40px;
    display: flex; align-items: center;
  }
  .holder { flex: 0 0 190px; text-align: right; padding-right: 16px; }
  .holder__name {
    color: var(--accent); font-weight: 700; font-size: 18px;
    text-transform: uppercase; letter-spacing: .5px;
  }
  .holder__title { color: var(--ink-light); font-size: 14px; margin-top: 4px; }
  .divider { width: 1px; height: 62px; background: var(--ink-muted); }
  .contact-list { list-style: none; padding-left: 14px; }
  .contact-list li {
    display: flex; align-items: center; gap: 7px;
    color: var(--ink-light); font-size: 12.5px; line-height: 1.6;
  }
  .contact-list svg { width: 11px; height: 11px; flex: none; }
</style>
</head>
<body>
<main class="stage">
  <section class="card card--front">
    <div class="wordmark">
      <span class="wordmark__main">Ridgeline</span>
      <span class="wordmark__sub">Hauling &amp; Logistics Inc.</span>
    </div>
    <div class="contact-block">
      <div class="holder">
        <p class="holder__name">Marcus Tillbrook</p>
        <p class="holder__title">President</p>
      </div>
      <div class="divider"></div>
      <ul class="contact-list">
        <li>
          <svg viewBox="0 0 12 12" aria-hidden="true"><path fill="#e3202a" d="M2.5 1l2 2.2-1 1.3a7 7 0 0 0 4 4l1.3-1 2.2 2-1.2 1.5C5.5 11 1 6.5 1 2.2z"/></svg>
          518-555-0147
        </li>
        <li>
          <svg viewBox="0 0 12 12" aria-hidden="true"><rect x="1" y="2.5" width="10" height="7" fill="#e3202a"/><path d="M1 2.5l5 4 5-4" stroke="#1f1f1f" fill="none"/></svg>
          ridgelinehaulingcompany@postvane.com
        </li>
        <li>
          <svg viewBox="0 0 12 12" aria-hidden="true"><circle cx="6" cy="6" r="5" fill="#e3202a"/><path d="M1 6h10M6 1c-2.5 3-2.5 7 0 10M6 1c2.5 3 2.5 7 0 10" stroke="#1f1f1f" fill="none" stroke-width=".8"/></svg>
          www.ridgelinehauling.com
        </li>
      </ul>
    </div>
  </section>

  <section class="card card--back">
    <div class="wordmark">
      <span class="wordmark__main">Ridgeline</span>
      <span class="wordmark__sub">Hauling &amp; Logistics Inc.</span>
    </div>
  </section>
</main>
</body>
</html>
```